Marlow Creek sign

24"x36" sign for new home construction job site. Located in affluent in-town neighborhood in Midwest. Traditional american style homes. 2nd generation construction company. Sign needs to convey strength and elegance but not overly elaborate. Competition most has signs consisting of text.

Sign text reads:
Marlow Creek Builders
Custom Luxury for Over 20 years
248-555-0137

Target Market(s)

Upper middle income home buyers

Industry/Entity Type

Construction

Font styles to use
Serif
Decorative

Requirements
Must have
• Logo image no more than 2 colors
Nice to have
• Should be visible and legible from distance of 30'
Should not have
• Not just image of house as logo

```html
<!DOCTYPE html>
<html lang="en">
<head>
<meta charset="utf-8">
<title>Marlow Creek Builders – Job Site Sign</title>
<link rel="stylesheet" href="https://fonts.googleapis.com/css2?family=Cormorant+Garamond:wght@500&family=EB+Garamond:wght@600&family=Open+Sans:wght@400&display=swap">
<style>
  :root {
    --page: #ffffff;
    --sign: #000000;
    --gold-dark: #a8862c;
    --gold-mid: #d4b458;
    --gold-light: #f3e3a6;
    --text: #ffffff;
  }
  html, body {
    margin: 0;
    padding: 0;
    width: 1200px;
    height: 1000px;
    overflow: hidden;
    background: var(--page);
  }
  .canvas {
    position: relative;
    width: 1200px;
    height: 1000px;
  }
  .sign-board {
    position: absolute;
    left: 10px;
    top: 66px;
    width: 1178px;
    height: 788px;
    background: var(--sign);
  }
  .gold-frame {
    position: absolute;
    left: 46px;
    top: 42px;
    width: 1080px;
    height: 704px;
    box-sizing: border-box;
    padding: 14px;
    background: linear-gradient(135deg, var(--gold-dark) 0%, var(--gold-light) 30%, var(--gold-mid) 55%, var(--gold-light) 80%, var(--gold-dark) 100%);
    border: 2px solid var(--gold-dark);
  }
  .frame-inner {
    width: 100%;
    height: 100%;
    box-sizing: border-box;
    background: var(--sign);
    border: 2px solid var(--gold-light);
    position: relative;
  }
  .brand-mark {
    position: absolute;
    left: 351px;
    top: 37px;
    width: 297px;
    height: 135px;
    background: linear-gradient(135deg, var(--gold-light) 0%, var(--gold-mid) 50%, var(--gold-dark) 100%);
    opacity: 0.85;
  }
  .divider {
    position: absolute;
    left: 166px;
    width: 645px;
    height: 5px;
    background: linear-gradient(90deg, rgba(212,180,88,0) 0%, var(--gold-mid) 20%, var(--gold-light) 50%, var(--gold-mid) 80%, rgba(212,180,88,0) 100%);
    clip-path: polygon(0 50%, 50% 0, 100% 50%, 50% 100%);
  }
  .divider-top { top: 190px; }
  .divider-bottom { top: 288px; }
  .company-name {
    position: absolute;
    left: 0;
    right: 0;
    top: 202px;
    margin: 0;
    text-align: center;
    font-family: "Cormorant Garamond", "Times New Roman", serif;
    font-weight: 500;
    font-size: 58px;
    line-height: 1.2;
    letter-spacing: 1.5px;
    color: var(--text);
  }
  .tagline {
    position: absolute;
    left: 0;
    right: 0;
    top: 376px;
    margin: 0;
    text-align: center;
    font-family: "EB Garamond", "Times New Roman", serif;
    font-weight: 600;
    font-variant: small-caps;
    font-variant-numeric: lining-nums;
    font-size: 55px;
    line-height: 1.2;
    letter-spacing: 1px;
    color: var(--text);
  }
  .phone-line {
    position: absolute;
    left: 244px;
    top: 511px;
    display: flex;
    align-items: center;
    gap: 18px;
  }
  .phone-icon {
    width: 88px;
    height: 88px;
  }
  .phone-number {
    font-family: "Open Sans", Arial, sans-serif;
    font-size: 54px;
    color: var(--text);
  }
</style>
</head>
<body>
<main class="canvas">
  <section class="sign-board">
    <div class="gold-frame">
      <div class="frame-inner">
        <div class="brand-mark" role="img" aria-label="Marlow Creek Builders rooftop brand mark in gold"></div>
        <div class="divider divider-top"></div>
        <h1 class="company-name">MARLOW CREEK BUILDERS</h1>
        <div class="divider divider-bottom"></div>
        <p class="tagline">Custom Luxury for Over 20 years</p>
        <div class="phone-line">
          <svg class="phone-icon" viewBox="0 0 88 88" aria-hidden="true">
            <defs>
              <linearGradient id="gold-grad" x1="0" y1="0" x2="1" y2="1">
                <stop offset="0" stop-color="#f3e3a6"/>
                <stop offset="0.5" stop-color="#c9a441"/>
                <stop offset="1" stop-color="#f3e3a6"/>
              </linearGradient>
            </defs>
            <circle cx="44" cy="44" r="40" fill="none" stroke="url(#gold-grad)" stroke-width="4"/>
            <path d="M50 20 l8 4 -4 10 -6 -2 c-4 6 -6 14 -5 22 l6 0 0 10 -9 2 c-8 -12 -6 -34 10 -46 z" fill="url(#gold-grad)"/>
          </svg>
          <span class="phone-number">248-555-0137</span>
        </div>
      </div>
    </div>
  </section>
</main>
</body>
</html>
```